We currently have a good logo and we want business cards that can display our logo but also represent our industry - telecom construction - We are a construction company specializing in telecom construction such as installation of fiber optic cable throughout cities and across the country. Nationwide services
We are large enough to handle most any project yet small enough to be a flexible partner and resource.

Target Market(s)

U.S. based telecom carriers and providers

Industry/Entity Type

Construction

Contact Information for Business Card

Business cards should include our logo, phone number and website address. Also, including some information as to our core services would be good.

Colors

Designer to choose colors to be used in the design.

Requirements
Must have
• Colors based on logo
• Must use our logo
• Logo, name, email, website address, phone number
• Tovek Subterra
• Brent Dacosta
• Director of Business Development
• (913) 555-0187
• www.tovekgrid.example
Nice to have
• Construction services including:
• Small Cell Construction
• Boring/Drilling
• Plowing / Trenching
• Conduit installation
• Fiber pulling
• splicing
• building entries
• Aerial construction
• Aerial Make Ready
• Make Ready Engineering
Should not have
• We are open to ideas

```html
<!DOCTYPE html>
<html lang="en">
<head>
<meta charset="utf-8">
<title>Tovek Subterra – Business Card</title>
<link rel="stylesheet" href="https://fonts.googleapis.com/css2?family=Montserrat:wght@400;500;700;800&family=Roboto+Condensed:wght@400;700&display=swap">
<style>
  :root {
    --stage: #262626;
    --blue-deep: #1257b0;
    --blue-mid: #1a78c9;
    --blue-light: #25aee6;
    --blue-ink: #1a5fb4;
    --white: #ffffff;
    --grey-text: #555a60;
    --grey-band: #8d8f93;
    --heading-brown: #7a4a3a;
  }
  * { box-sizing: border-box; margin: 0; padding: 0; }
  html, body { width: 1200px; height: 900px; overflow: hidden; }
  body {
    background: var(--stage);
    font-family: "Montserrat", sans-serif;
    position: relative;
  }
  .card {
    position: absolute;
    left: 290px;
    width: 620px;
    height: 354px;
    overflow: hidden;
  }

  /* Back of card */
  .card-back {
    top: 60px;
    background: linear-gradient(100deg, var(--blue-deep) 0%, var(--blue-mid) 35%, var(--blue-light) 55%, var(--blue-mid) 75%, var(--blue-deep) 100%);
    color: var(--white);
  }
  .back-brand {
    position: absolute;
    left: 56px;
    top: 156px;
    width: 260px;
    font-weight: 800;
    font-size: 26px;
    line-height: 32px;
    white-space: nowrap;
    color: var(--white);
    display: flex;
    align-items: center;
    gap: 10px;
  }
  .back-brand .mark-square { width: 14px; height: 14px; background: var(--white); flex: none; }
  .back-divider {
    position: absolute;
    left: 330px;
    top: 70px;
    width: 2px;
    height: 200px;
    background: rgba(122, 74, 58, 0.8);
  }
  .services {
    position: absolute;
    left: 350px;
    top: 70px;
    font-family: "Roboto Condensed", sans-serif;
  }
  .services-heading {
    font-size: 15px;
    color: var(--heading-brown);
    margin-bottom: 2px;
  }
  .services-list { list-style: none; }
  .services-list li {
    font-size: 16px;
    line-height: 18.5px;
    position: relative;
    padding-left: 20px;
  }
  .services-list li::before {
    content: "";
    position: absolute;
    left: 2px;
    top: 5px;
    width: 9px;
    height: 9px;
    border-radius: 50%;
    background: var(--white);
  }

  /* Front of card */
  .card-front {
    top: 456px;
    background: var(--white);
  }
  .front-brand {
    position: absolute;
    left: 48px;
    top: 42px;
    font-weight: 800;
    font-size: 34px;
    color: var(--blue-ink);
    display: flex;
    align-items: center;
    gap: 10px;
  }
  .front-brand .mark-square { width: 14px; height: 14px; background: var(--blue-ink); }
  .person-name {
    position: absolute;
    left: 48px;
    top: 118px;
    font-weight: 800;
    font-size: 28px;
    color: var(--blue-ink);
    letter-spacing: 0.5px;
  }
  .person-title {
    position: absolute;
    left: 48px;
    top: 154px;
    font-family: "Roboto Condensed", sans-serif;
    font-size: 19px;
    color: var(--grey-text);
  }
  .rule {
    position: absolute;
    left: 40px;
    top: 190px;
    width: 520px;
    height: 3px;
    background: var(--blue-mid);
  }
  .rule-end {
    position: absolute;
    left: 560px;
    top: 185px;
    width: 22px;
    height: 13px;
    border-radius: 2px;
    background: linear-gradient(180deg, #c6c8cc, #7f8287);
  }
  .contacts {
    position: absolute;
    left: 40px;
    top: 212px;
    list-style: none;
  }
  .contacts li {
    display: flex;
    align-items: center;
    gap: 12px;
    font-size: 20px;
    line-height: 30px;
    color: var(--grey-text);
  }
  .contacts svg { width: 20px; height: 20px; flex: none; }
  .band-blue {
    position: absolute;
    left: 0;
    bottom: 0;
    width: 320px;
    height: 34px;
    background: linear-gradient(90deg, var(--blue-deep), var(--blue-light));
    clip-path: polygon(0 0, 94% 0, 100% 100%, 0 100%);
  }
  .band-grey {
    position: absolute;
    left: 318px;
    bottom: 0;
    width: 302px;
    height: 14px;
    background: var(--grey-band);
  }
</style>
</head>
<body>

<section class="card card-back" aria-label="Back of card">
  <div class="back-brand"><span class="mark-square"></span>Tovek Subterra</div>
  <div class="back-divider"></div>
  <div class="services">
    <p class="services-heading">Construction services including:</p>
    <ul class="services-list">
      <li>Small Cell Construction</li>
      <li>Boring/Drilling</li>
      <li>Plowing / Trenching</li>
      <li>Conduit installation</li>
      <li>Fiber pulling</li>
      <li>splicing</li>
      <li>building entries</li>
      <li>Aerial construction</li>
      <li>Aerial Make Ready</li>
      <li>Make Ready Engineering</li>
    </ul>
  </div>
</section>

<section class="card card-front" aria-label="Front of card">
  <div class="front-brand"><span class="mark-square"></span>Tovek Subterra</div>
  <h1 class="person-name">BRENT DACOSTA</h1>
  <p class="person-title">Director of Business Development</p>
  <div class="rule"></div>
  <div class="rule-end" role="img" aria-label="Cable connector end"></div>
  <ul class="contacts">
    <li>
      <svg viewBox="0 0 24 24" fill="none" stroke="#1a78c9" stroke-width="2" stroke-linecap="round" stroke-linejoin="round"><path d="M22 16.9v3a2 2 0 0 1-2.2 2 19.8 19.8 0 0 1-8.6-3.1 19.5 19.5 0 0 1-6-6A19.8 19.8 0 0 1 2.1 4.2 2 2 0 0 1 4.1 2h3a2 2 0 0 1 2 1.7c.1.9.4 1.8.7 2.7a2 2 0 0 1-.5 2.1L8 9.8a16 16 0 0 0 6 6l1.3-1.3a2 2 0 0 1 2.1-.4c.9.3 1.8.6 2.7.7a2 2 0 0 1 1.7 2z"/></svg>
      (913) 555-0187
    </li>
    <li>
      <svg viewBox="0 0 24 24" fill="none" stroke="#1a78c9" stroke-width="2" stroke-linejoin="round"><rect x="2" y="5" width="20" height="14" rx="1"/><path d="M2 6l10 7 10-7"/></svg>
      info@brentdacosta.example
    </li>
    <li>
      <svg viewBox="0 0 24 24" fill="none" stroke="#1a78c9" stroke-width="2"><circle cx="12" cy="12" r="10"/><path d="M2 12h20M12 2c3 3 3 17 0 20M12 2c-3 3-3 17 0 20"/></svg>
      www.tovekgrid.example
    </li>
  </ul>
  <div class="band-grey"></div>
  <div class="band-blue"></div>
</section>

</body>
</html>
```